Business Card Design Project

I want a design for my business cards based on an excisting logo design.

Target Market(s)

Marketeers, PR-peeps, CEO's, decisionmakers, entrepreneurs

Industry/Entity Type

Business

Requirements
Nice to have
• Some visual interest on the back too
Should not have
• Sarif on the font

```html
<!DOCTYPE html>
<html lang="nl">
<head>
<meta charset="utf-8">
<title>LeafLine PR – visitekaartje</title>
<link rel="stylesheet" href="https://fonts.googleapis.com/css2?family=Fira+Sans:wght@300;400;500&display=swap">
<style>
  :root {
    --leaf-green: #aecb0b;
    --link-green: #4f9a1c;
    --paper: #ffffff;
    --ink: #2f3a12;
    --wordmark-grey: #8a8a8a;
  }
  * { box-sizing: border-box; margin: 0; padding: 0; }
  html, body {
    width: 1200px;
    height: 900px;
    overflow: hidden;
    background: var(--paper);
    font-family: "Fira Sans", Arial, sans-serif;
  }
  .canvas {
    position: relative;
    width: 1200px;
    height: 900px;
  }
  .card {
    position: absolute;
    left: 304px;
    width: 592px;
    text-align: center;
  }

  /* Front */
  .card-front {
    top: 104px;
    height: 330px;
    background: var(--leaf-green);
    border-radius: 34px;
    padding: 16px;
  }
  .card-front__inner {
    position: relative;
    width: 100%;
    height: 100%;
    background: var(--paper);
    border-radius: 22px;
  }
  .brand-dot {
    position: absolute;
    left: 50%;
    top: 42px;
    width: 150px;
    height: 150px;
    margin-left: -75px;
    border-radius: 50%;
    background: var(--leaf-green);
  }
  .brand-name {
    position: absolute;
    left: 0;
    right: 0;
    top: 212px;
    font-size: 44px;
    font-weight: 300;
    letter-spacing: 1px;
    color: var(--wordmark-grey);
  }
  .web-links {
    position: absolute;
    left: 0;
    right: 0;
    top: 270px;
    font-size: 14px;
    font-weight: 400;
    color: var(--link-green);
  }
  .web-links .sep { margin: 0 6px; }

  /* Back */
  .card-back {
    top: 464px;
    height: 332px;
    background: var(--leaf-green);
    border-radius: 32px;
    color: var(--ink);
  }
  .back-brand {
    position: absolute;
    left: 0; right: 0;
    top: 44px;
    font-size: 54px;
    font-weight: 400;
    color: var(--paper);
  }
  .tagline {
    position: absolute;
    left: 0; right: 0;
    top: 116px;
    font-size: 17px;
    font-weight: 400;
  }
  .person-name {
    position: absolute;
    left: 0; right: 0;
    top: 142px;
    font-size: 29px;
    font-weight: 400;
  }
  .contact {
    position: absolute;
    left: 0; right: 0;
    top: 180px;
    font-size: 19px;
    line-height: 21px;
    font-weight: 400;
  }
  .address {
    position: absolute;
    left: 0; right: 0;
    top: 278px;
    font-size: 14px;
    font-weight: 400;
  }
</style>
</head>
<body>
<main class="canvas">
  <section class="card card-front" aria-label="Voorkant visitekaartje">
    <div class="card-front__inner">
      <span class="brand-dot" aria-hidden="true"></span>
      <h1 class="brand-name">LeafLine PR</h1>
      <p class="web-links">
        leaflinepr.nl<span class="sep">|</span>social.example/_leaflinepr<span class="sep">|</span>social.example/leaflinepr
      </p>
    </div>
  </section>

  <section class="card card-back" aria-label="Achterkant visitekaartje">
    <h2 class="back-brand">LeafLine PR</h2>
    <p class="tagline">Systemisch en strategisch PR, marketing en communicatieadvies</p>
    <p class="person-name">Marit Jansen</p>
    <p class="contact">marit.jansen@leaflinepr.nl<br>+31 (0)6 5550 1234</p>
    <p class="address">Lindelaan 12, 6700 AB Voorstad</p>
  </section>
</main>
</body>
</html>
```